Vantri Almond Protein - Less, but better

Design a protein powder pouch (350g). Take inspiration from Parvenix.co and put the same information on the pouch and add "made in Australia". I do not want it to be exactly the same design but just take some inspiration from it.

```html
<!DOCTYPE html>
<html lang="en">
<head>
<meta charset="utf-8">
<title>Vantri Almond Protein Pouch Label</title>
<link rel="stylesheet" href="https://fonts.googleapis.com/css2?family=Anton&family=Montserrat:wght@400;500;600;700&display=swap">
<style>
  :root {
    --forest: #1e3a31;
    --sage: #789d8f;
    --mustard: #f1a300;
    --cream: #f7f3e6;
    --blush: #e4a59f;
  }
  html, body { margin: 0; padding: 0; overflow: hidden; }
  body { width: 743px; height: 1200px; background: var(--forest); }
  .label {
    position: relative; width: 743px; height: 1200px; overflow: hidden;
    font-family: "Montserrat", sans-serif; color: var(--forest);
  }
  .label-art { position: absolute; inset: 0; }
  .centered { position: absolute; left: 0; width: 743px; text-align: center; margin: 0; }
  .brand-name {
    top: 258px; font-size: 104px; font-weight: 700; color: var(--cream);
    letter-spacing: -2px; line-height: 1;
  }
  .tagline { top: 412px; font-size: 31px; font-weight: 500; color: var(--cream); letter-spacing: 2px; }
  .definition { top: 462px; font-size: 19px; font-weight: 400; color: var(--cream); }
  .origin {
    position: absolute; left: 215px; top: 514px; margin: 0;
    font-size: 17px; font-weight: 700; color: var(--blush);
  }
  .product-line-1 { top: 586px; font-size: 58px; font-weight: 700; line-height: 1; }
  .product-line-2 {
    top: 656px; font-family: "Anton", sans-serif; font-size: 98px; line-height: 1;
    color: var(--blush); transform: scaleX(1.3);
  }
  .product-line-3 { top: 764px; font-size: 58px; font-weight: 700; line-height: 1; }
  .flavour {
    position: absolute; left: 229px; top: 826px; width: 286px; height: 45px;
    background: var(--blush); color: var(--cream); margin: 0;
    font-size: 26px; font-weight: 700; line-height: 45px; text-align: center;
  }
  .claims { top: 884px; font-size: 16px; font-weight: 500; }
  .benefits-title {
    position: absolute; left: 247px; top: 981px; width: 248px; height: 43px;
    background: var(--forest); color: var(--cream); border-radius: 5px; margin: 0;
    font-size: 25px; font-weight: 700; line-height: 43px; text-align: center;
  }
  .benefits-list {
    position: absolute; left: 151px; top: 1036px; width: 441px; height: 38px;
    border-top: 2px solid var(--cream); border-bottom: 2px solid var(--cream);
    margin: 0; color: var(--cream); font-size: 15px; font-weight: 700;
    line-height: 38px; text-align: center; white-space: nowrap;
  }
  .net-weight { top: 1093px; font-size: 15px; font-weight: 700; color: var(--cream); }
</style>
</head>
<body>
<main class="label">
  <svg class="label-art" width="743" height="1200" viewBox="0 0 743 1200" aria-hidden="true">
    <rect width="743" height="1200" fill="var(--forest)"/>
    <circle class="sun-disc" cx="743" cy="0" r="210" fill="var(--mustard)"/>
    <circle class="side-arc" cx="0" cy="420" r="150" fill="var(--sage)"/>
    <path class="lower-panel" fill="var(--blush)" d="M0 640 Q0 590 50 590 H693 Q743 590 743 640 V1200 H0 Z"/>
    <rect class="product-panel" x="150" y="548" width="443" height="402" rx="40" fill="var(--cream)"/>
    <circle class="corner-disc" cx="743" cy="1200" r="180" fill="var(--mustard)"/>
    <circle class="corner-arc" cx="0" cy="1200" r="120" fill="var(--sage)"/>
    <g class="product-frame" fill="none" stroke="var(--forest)" stroke-width="2.5">
      <path d="M208 662 V572 Q208 560 220 560 H518 Q530 560 530 572 V662"/>
      <path d="M208 772 V908 Q208 920 220 920 H518 Q530 920 530 908 V772"/>
    </g>
  </svg>

  <h1 class="centered brand-name">vantri</h1>
  <p class="centered tagline">–less, but better–</p>
  <p class="centered definition">adj. In pursuit of health and happiness.</p>
  <p class="origin">MADE IN AUSTRALIA</p>

  <p class="centered product-line-1">ALMOND</p>
  <p class="centered product-line-2">PROTEIN</p>
  <p class="centered product-line-3">POWDER</p>
  <p class="flavour">REAL VANILLA</p>
  <p class="centered claims">Vegan Just 4 Ingredients Delicious</p>

  <p class="benefits-title">Supports Health:</p>
  <p class="benefits-list">Heart Digestion &nbsp;|&nbsp; Immune System &nbsp;|&nbsp; kin-Bone-Hair</p>
  <p class="centered net-weight">Net WT. 12 OZ (340g)</p>
</main>
</body>
</html>
```